Web Design & Programming for Health & Wellness Coaching Company (PageFoundry or Scribeloom)

Business Info: I'm starting a health coaching business (Colette Marsh, PhD, Health & Wellness Coaching @ colettemarshwell.com) and need some help designing my website (colettemarshwell.com).

Basics: I have the domain purchased on pagefoundry.com that is also linked to Scribeloom (so designer/programmer can program into pagefoundry.com or Scribeloom.com). I want my primary color to be aqua blue (see 1st photo/pdf attached) and my secondary colors to be spring green (1) and deep purple/magenta (see 2nd photo/pdf attached as well as the last photo attached).

There will be 5 pages: 1) Home; 2) Services; 3) Coaching Philosophy; 4) About Me; 5) Blog; 6) Client Resources; 7) Contact Me

I want there to be a banner at the top of each page, on the right-hand side (align right) that has links to all other pages, as well as a “book a consult” icon (that links to an appointment book where clients can see my schedule and book an appointment) and a cart icon, where clients can check out and pay. The cart will need to be linked to a pay service. The banner should roughly appear as follows:
Home | Services | Coaching Philosophy | About Me | [Book a Consult Icon] | [Cart Icon]

I also want there to be a small, centered area for hyperlinks at the bottom of each page that appears as follows (with everything hyperlinked):

Home | Services | Coaching Philosophy | About Me
555-314-2786 | colette@colettemarshwell.com
Colette Marsh, PhD, LLC | © 2022

“Home Page:” I would like my home page to have 3-4 main aspects: 1) a marquis of photos of me (included below; one main photo, but with options for clients to right/left click to scroll through several photos); 2-3) space for text about my coaching philosophy and program 3) a marquis of client testimonials that clients can scroll through. I like the setup of this homepage: https://www.tidewellcoach.example but using my color scheme (below). I want the home page to have the water background shown in the first image (but not the surfers).

“Services page:” I offer the following 5 services: 1) Free Health History Consultation; 2) Standard 6-Month Program; 3) Deluxe 6-Month Program; 4) Coastal Calm Insight Card Reading; 5) Customized Options.

I want each service to be shown on the Services page and to contain a “Book Appointment” or “Purchase” button/link (Services #1-2 should have the “Book appointment” button and services #3-5 should have the “Purchase” button). I want the “Book appointment” button to link to a calendar where clients can see my schedule and book an appointment. Both links should also cause the item to appear in the cart, and the cart should be linked to a pay feature that can take clients’ credit card info, etc.

The “About Me” Page should say “About Me” then have 1 photo (with arrow options on both sides so clients can scroll through different photos). Below the photo should be a block of text where I can include a few paragraphs about me. Below the text should be links to the following pages, which can appear as follows:

Find Me on Social Media:
Current: https://olvera-institute.example/profile/cmarsh
ConnectWork: https://www.connectworknet.example/in/colette-marsh-52718406/
FriendSpace: https://www.friendspace.example/colette.marsh
SnapGallery: https://www.snapgallery.example/colettem_hikes/?hl=en

The “Coaching Philosophy” page should be similar to the “About Me” page (minus the “Follow Me on social media” part). This page should have 2 icon/links below the text: 1 that says “Let’s Get Started” and directs patients to my calendar where they can book a free 1hr health coaching consultation; 1 that says “Book a Service” and takes clients to the services page.

The “Blog” page will be a standard blog page.

The “Client Resources” page will be for client resources. I would like for this page to require clients to enter their a login name and password (provided by me).

More about my business:
My health coaching certification is through the Academy of Holistic Dietetics (AHD, holisticdieteticsacademy.com). I also have a PhD in Basic Biomedical Science & Neuroscience (specializing in addiction) and post-doctorate experience at the Olvera Institute of Botanical Healing in alternative/complementary and integrative health interventions for binge eating and obesity (things like 12-step interventions, yoga, acupuncture, meditation, herbs, etc.).

My health coaching practice centers around 2 concepts: 1) the client can heal his/herself by him/herself; I am simply here to help the client tap into his/her own healing intuition; 2) I believe in wholistic healing that brings primary and secondary foods into balance. Secondary foods are the foods we put on our plate and eat. Primary foods are everything else in our life that nourishes us (e.g., creativity, relationships, movement, joy, finances, etc.). When the secondary foods are a problem, it's usually a sign that our primary foods are imbalanced, so I help clients identify how to rebalance both.

I also included some sample photos that will on the "about me" page of my website. I focus on connection, movement, and nature, so lots of nature themes. Mountains.

Here are some other relevant "about me" websites:

Target Market(s)

Adult females and males who live busy lives and want help and support in creating transformation and breakthroughs, on their plates (nutrition) and in their lives.

Industry/Entity Type

Health and Wellness

Number of Pages Required

5+ page

Font styles to use
Serif
Sans Serif

Colors
0094D4
00A9DD
6FCCEA
C7EBF8
E9F6FB

Requirements
Must have
• See project description
Nice to have
• See project description

```html
<!DOCTYPE html>
<html lang="en">
<head>
<meta charset="utf-8">
<title>Colette Marsh, PhD, Health &amp; Wellness Coaching</title>
<link href="https://fonts.googleapis.com/css2?family=Raleway:wght@600;700&family=Poppins:wght@300;400;500;600&display=swap" rel="stylesheet">
<style>
:root{
  --aqua:#00A9DD;
  --aqua-deep:#0094D4;
  --aqua-light:#6FCCEA;
  --ink:#1f1f1f;
  --muted:#7a7a7a;
  --footer:#232323;
  --white:#ffffff;
  --sea-1:#0b4752;
  --sea-2:#0f6470;
  --sea-3:#0a3a45;
}
*{margin:0;padding:0;box-sizing:border-box}
html,body{width:1200px;height:2752px;overflow:hidden}
body{font-family:"Poppins",sans-serif;color:var(--ink);background:var(--white);position:relative}

.hero{position:absolute;left:0;top:0;width:1200px;height:1520px;overflow:hidden}
.hero-bg{position:absolute;inset:0;background:
  radial-gradient(ellipse at 30% 20%,rgba(40,140,150,.55),transparent 55%),
  radial-gradient(ellipse at 80% 60%,rgba(20,110,125,.5),transparent 60%),
  linear-gradient(180deg,var(--sea-2) 0%,var(--sea-1) 45%,var(--sea-3) 100%)}

.site-header{position:absolute;left:0;top:0;width:1200px;height:110px}
.brand{position:absolute;left:76px;top:40px;color:var(--white);font-family:"Poppins",sans-serif;font-weight:600;font-size:26px;letter-spacing:.5px}
.main-nav{position:absolute;left:418px;top:50px;display:flex;gap:34px}
.main-nav a{color:var(--white);text-decoration:none;font-size:15px;font-weight:400}
.btn-consult{position:absolute;left:880px;top:40px;width:162px;height:38px;border-radius:4px;background:var(--aqua);color:var(--white);font-size:14px;font-weight:500;display:flex;align-items:center;justify-content:center;text-decoration:none}
.cart{position:absolute;left:1104px;top:44px}

.hero-title{position:absolute;left:0;width:1200px;top:236px;text-align:center;color:var(--white);font-family:"Raleway",sans-serif;font-weight:700;font-size:72px}
.hero-sub{position:absolute;left:0;width:1200px;top:372px;display:flex;align-items:center;justify-content:center;gap:30px;color:var(--white);font-size:28px;letter-spacing:14px;font-weight:400}
.hero-sub .rule{width:150px;height:2px;background:var(--white)}

.portrait-ring{position:absolute;left:426px;top:548px;width:348px;height:348px;border-radius:50%;border:3px solid var(--white);padding:14px}
.portrait{width:100%;height:100%;border-radius:50%;background:radial-gradient(circle at 50% 40%,#c9a98a 0%,#8d8f86 45%,#4f6d72 100%)}
.arrow{position:absolute;top:700px;width:58px;height:58px;border-radius:50%;background:var(--white);display:flex;align-items:center;justify-content:center}
.arrow.prev{left:330px}.arrow.next{left:828px}

.coach-name{position:absolute;left:0;width:1200px;top:1018px;text-align:center;color:var(--white);font-family:"Raleway",sans-serif;font-weight:700;font-size:56px}
.coach-role{position:absolute;left:0;width:1200px;top:1098px;text-align:center;color:var(--aqua-light);font-size:20px}
.coach-bio{position:absolute;left:270px;width:660px;top:1176px;text-align:center;color:var(--white);font-size:16px;line-height:30px}

.testimonials{position:absolute;left:0;top:1520px;width:1200px;height:820px;background:var(--white)}
.testimonials h2{position:absolute;left:122px;top:204px;font-family:"Raleway",sans-serif;font-weight:600;font-size:66px;color:var(--ink)}
.quote-text{position:absolute;left:122px;top:336px;width:440px;font-size:16px;line-height:34px;color:var(--muted)}
.quote-author{position:absolute;left:122px;top:642px;font-size:18px;font-weight:500;color:var(--ink)}
.quote-role{position:absolute;left:282px;top:646px;font-size:14px;color:var(--aqua)}
.quote-mark{position:absolute;left:556px;top:632px}
.photo-frame{position:absolute;left:720px;top:150px;width:392px;height:522px;border:4px solid var(--aqua);border-radius:24px}
.photo{position:absolute;left:700px;top:172px;width:392px;height:522px;border-radius:20px;background:linear-gradient(170deg,#6e9bc6 0%,#8fb2a0 35%,#7a8a5c 65%,#b08a72 100%)}

.site-footer{position:absolute;left:0;top:2340px;width:1200px;height:412px;background:var(--footer);color:var(--white);text-align:center}
.footer-brand{position:absolute;left:0;width:1200px;top:84px;font-weight:600;font-size:24px}
.footer-nav{position:absolute;left:0;width:1200px;top:152px;font-size:14px;color:#bdbdbd}
.footer-nav a{color:#bdbdbd}
.footer-social{position:absolute;left:0;width:1200px;top:204px;display:flex;justify-content:center;gap:22px}
.footer-social span{width:16px;height:16px;border-radius:50%;background:var(--white);display:block}
.footer-contact{position:absolute;left:0;width:1200px;top:256px;font-size:13px;line-height:26px;color:#bdbdbd}
.footer-strip{position:absolute;left:0;bottom:0;width:1200px;height:12px;background:var(--aqua)}
</style>
</head>
<body>

<section class="hero">
  <div class="hero-bg" role="img" aria-label="Deep teal ocean water background"></div>

  <header class="site-header">
    <div class="brand">colettemarshwell</div>
    <nav class="main-nav">
      <a href="#">Home</a><a href="#">Services</a><a href="#">Coaching Philosophy</a><a href="#">About Me</a>
    </nav>
    <a class="btn-consult" href="#">Book a Consultation</a>
    <svg class="cart" width="26" height="28" viewBox="0 0 26 28" fill="none" stroke="#fff" stroke-width="2">
      <path d="M4 9h18l-1.5 16h-15z"/><path d="M9 11V6a4 4 0 0 1 8 0v5"/>
    </svg>
  </header>

  <h1 class="hero-title">Health &amp; Wellness</h1>
  <div class="hero-sub"><span class="rule"></span>COACHING<span class="rule"></span></div>

  <div class="portrait-ring"><div class="portrait" role="img" aria-label="Portrait photo of Colette Marsh"></div></div>
  <a class="arrow prev" href="#"><svg width="16" height="16" viewBox="0 0 16 16"><path d="M10 2 4 8l6 6" fill="none" stroke="#222" stroke-width="2.5"/></svg></a>
  <a class="arrow next" href="#"><svg width="16" height="16" viewBox="0 0 16 16"><path d="M6 2l6 6-6 6" fill="none" stroke="#222" stroke-width="2.5"/></svg></a>

  <h2 class="coach-name">Colette Marsh</h2>
  <p class="coach-role">PhD, Health &amp; Wellness Coaching</p>
  <p class="coach-bio">My health coaching certification is through the Academy of Holistic Dietetics (AHD, holisticdieteticsacademy.com). I also have a PhD in Basic Biomedical Science &amp; Neuroscience (specializing in addiction) and post-doctorate experience at the Olvera Institute of Botanical Healing in alternative/complementary and integrative health interventions for binge eating and obesity (things like 12-step interventions, yoga, acupuncture, meditation, herbs, etc.).</p>
</section>

<section class="testimonials">
  <h2>Testimonials</h2>
  <p class="quote-text">My health coaching certification is through the Academy of Holistic Dietetics (AHD, holisticdieteticsacademy.com). I also have a PhD in Basic Biomedical Science &amp; Neuroscience (specializing in addiction) and post-doctorate experience at the Olvera</p>
  <p class="quote-author">Reid Calloway</p>
  <p class="quote-role">Friend</p>
  <svg class="quote-mark" width="40" height="32" viewBox="0 0 40 32" fill="#00A9DD">
    <path d="M0 32V18C0 8 5 2 14 0l2 4c-5 2-7 6-7 10h7v18zM22 32V18c0-10 5-16 14-18l2 4c-5 2-7 6-7 10h7v18z"/>
  </svg>
  <div class="photo-frame"></div>
  <div class="photo" role="img" aria-label="Photo of Colette hiking on a mountain trail"></div>
</section>

<footer class="site-footer">
  <div class="footer-brand">colettemarshwell</div>
  <p class="footer-nav"><a href="#">Home</a> | <a href="#">Services</a> | <a href="#">Coaching Philosophy</a> | <a href="#">About Me</a></p>
  <div class="footer-social"><span></span><span></span><span></span></div>
  <p class="footer-contact">555-314-2786 | colette@colettemarshwell.com<br>Colette Marsh, PhD, LLC | © 2022</p>
  <div class="footer-strip"></div>
</footer>

</body>
</html>
```